The Plain Harvest Plate: Reshape Your Bond with Eating in Only 30 Days

I want a book cover for a paperback non-fiction book 30 day challenge to transform you relationship with your food, diet and lifestyle for longterm health and vitality. I would like to incorporate two photos on the front cover, one of a Greek salad and one of me the author. I have uploaded the four photos. Use which of each pair you think best. Because of my name, I want the photo on the cover. Otherwise folks assume Marla is a guy.
I am looking at best selling health books and they seem to be on the lighter side color-wise, with horizontal design. Green and orange seem to work most often, though my logo is a bluish turquoise (https://marlaquent.com). I would imagine a light background, clear simple fonts. Looking forward to your designs!

Target Market(s)

Women around 35-40 confused by conflicting nutrition information but dedicated to better health haelthy

Industry/Entity Type

nutrition and wellness

Font styles to use
Serif

Colors
00AB8E
00BBA5
67D7C9
C6EFE9
E9F9F6
F0912C
F2A743
F7CA91
FBE8D2
FDF5EE
EE7325
F08F49
F5BC92
FAE3D3
FDF4ED

Requirements
Must have
• Clear simple look with room for an endorsement
Nice to have
• Hints of natural scenes and happy places
Should not have
• Dark or ominous feel

```html
<!DOCTYPE html>
<html lang="en">
<head>
<meta charset="utf-8">
<title>The Plain Harvest Plate – Book Cover Wrap</title>
<link rel="stylesheet" href="https://fonts.googleapis.com/css2?family=Raleway:wght@400;500;600;700&display=swap">
<style>
  :root {
    --stage: #2e2f30;
    --paper: #ffffff;
    --teal: #1597a6;
    --ink-grey: #66686b;
    --body-ink: #333333;
    --placeholder: #e6e6e6;
    --salad-green: #d3d7a6;
    --counter: #d6cfc4;
    --jacket-cream: #e4d3ad;
  }
  * { box-sizing: border-box; margin: 0; padding: 0; }
  html, body { width: 1200px; height: 1000px; overflow: hidden; }
  body {
    background: var(--stage);
    position: relative;
    font-family: "Raleway", Arial, sans-serif;
  }
  .panel { position: absolute; background: var(--paper); overflow: hidden; }

  /* Back cover */
  .back-cover { left: 73px; top: 143px; width: 482px; height: 742px; }
  .back-title {
    position: absolute; left: 43px; top: 40px;
    font-size: 30px; font-weight: 500; color: var(--ink-grey); letter-spacing: -0.2px;
  }
  .back-title .accent { color: var(--teal); }
  .blurb {
    position: absolute; left: 43px; top: 88px; width: 395px;
    font-size: 9.6px; line-height: 14.2px; color: var(--body-ink);
    text-align: justify;
  }
  .blurb p + p { margin-top: 14px; }
  .author-photo-back {
    position: absolute; left: 43px; top: 477px; width: 135px; height: 140px;
    background: linear-gradient(180deg, #f5f4f2 0%, #ebe6e1 55%, #8d8682 78%, #3b3a3e 100%);
  }
  .bio {
    position: absolute; left: 196px; top: 475px; width: 242px;
    font-size: 9.6px; line-height: 15px; color: var(--body-ink); text-align: justify;
  }
  .isbn-box {
    position: absolute; left: 287px; top: 617px; width: 175px; height: 103px;
    background: var(--placeholder); z-index: 2;
  }
  .back-band {
    position: absolute; left: 0; bottom: 0; width: 100%; height: 87px;
    background: var(--teal);
  }
  .back-url {
    position: absolute; left: 43px; bottom: 36px;
    font-size: 13px; letter-spacing: 2px; color: #fff; font-weight: 500;
  }

  /* Spine */
  .spine { left: 585px; top: 143px; width: 43px; height: 742px; }
  .spine-title, .spine-author {
    position: absolute; left: 50%; white-space: nowrap;
    transform-origin: left center;
    transform: rotate(90deg) translateY(-50%);
    font-size: 23px; font-weight: 500; color: var(--ink-grey);
  }
  .spine-title { top: 60px; }
  .spine-title .accent { color: var(--teal); }
  .spine-mark { position: absolute; left: 14px; top: 420px; width: 15px; height: 15px; border-radius: 50%; background: var(--teal); }
  .spine-author { top: 460px; }
  .spine-band { position: absolute; left: 0; bottom: 0; width: 100%; height: 87px; background: var(--teal); }

  /* Front cover */
  .front-cover { left: 653px; top: 143px; width: 482px; height: 742px; }
  .kitchen-scene {
    position: absolute; left: 0; top: 190px; width: 100%; height: 465px;
    background:
      linear-gradient(180deg, #ffffff 0%, rgba(255,255,255,0) 40%),
      linear-gradient(115deg, var(--salad-green) 0%, #dfe0bd 45%, var(--counter) 75%, #cfc7bc 100%);
  }
  .front-title {
    position: absolute; left: 42px; top: 78px;
    font-weight: 500; line-height: 1; letter-spacing: -1px;
  }
  .front-title span { display: block; }
  .front-title .small { font-size: 44px; color: var(--ink-grey); }
  .front-title .big { font-size: 80px; color: var(--teal); margin-top: -2px; }
  .front-title .end { font-size: 80px; color: var(--ink-grey); margin-top: -2px; }
  .promise-badge { position: absolute; left: 283px; top: 40px; width: 172px; height: 172px; }
  .badge-text {
    position: absolute; left: 296px; top: 74px; width: 146px;
    text-align: center; color: #fff; font-size: 14.5px; line-height: 16px; font-weight: 500;
  }
  .badge-text strong { display: block; font-size: 28px; line-height: 32px; font-weight: 700; }
  .front-band {
    position: absolute; left: 0; bottom: 0; width: 100%; height: 87px;
    background: var(--teal);
  }
  .front-author {
    position: absolute; left: 43px; bottom: 27px;
    font-size: 33px; font-weight: 600; color: #fff;
  }
  .author-photo-front {
    position: absolute; left: 272px; top: 467px; width: 210px; height: 275px;
    background: linear-gradient(180deg, #eee9e2 0%, #e9dfcc 50%, var(--jacket-cream) 100%);
  }
</style>
</head>
<body>

  <section class="panel back-cover">
    <h2 class="back-title">The <span class="accent">Plain Harvest</span> Plate</h2>
    <div class="blurb">
      <p>Lorem ipsum dolor sit amet, consectetur adipiscing elit, sed do eiusmod tempor incididunt ut labore et dolore magna aliqua. Imperdiet nulla malesuada pellentesque elit. Dui nunc mattis enim ut tellus elementum sagittis. Ante metus dictum at tempor commodo ullamcorper. Pretium quam vulputate dignissim suspendisse in est. Facilisis magna etiam tempor orci eu lobortis elementum. Mollis aliquam ut porttitor leo a diam sollicitudin. Enim praesent elementum facilisis leo. Pharetra diam sit amet nisl suscipit. Egestas tellus rutrum tellus pellentesque eu tincidunt. In aliquam sem fringilla ut morbi tincidunt augue. Pellentesque habitant morbi tristique senectus et netus et. Morbi tincidunt ornare massa eget egestas purus. Nulla facilisi morbi tempus iaculis urna id volutpat. Eu facilisis sed odio morbi quis commodo odio aenean sed. Lacus sed viverra tellus in hac habitasse platea. Lectus quam id leo in vitae turpis massa.</p>
      <p>Habitant morbi tristique senectus et netus et malesuada fames. Urna porttitor rhoncus dolor purus non enim praesent elementum. Ut sem nulla pharetra diam sit amet nisl suscipit. Quam id leo in vitae turpis massa sed elementum. Odio aenean sed adipiscing diam donec. Nunc faucibus a pellentesque sit amet porttitor eget. Dolor sit amet consectetur adipiscing elit duis tristique sollicitudin. Integer malesuada nunc vel risus. Sit amet consectetur adipiscing elit. Ipsum faucibus vitae aliquet nec ullamcorper sit. Netus et malesuada fames ac turpis egestas integer eget. Eget magna fermentum iaculis eu non diam phasellus. Sit amet nisl suscipit adipiscing bibendum est. Aenean sed adipiscing diam donec adipiscing tristique risus nec. Pharetra sit amet aliquam id. Libero nunc consequat interdum varius sit amet mattis vulputate enim. Etiam sit amet nisl purus in mollis nunc. Vitae aliquet nec ullamcorper sit amet risus nullam. Arcu cursus euismod quis viverra nibh cras pulvinar mattis nunc. Amet tellus cras adipiscing enim eu turpis.</p>
    </div>
    <div class="author-photo-back" role="img" aria-label="Portrait photo of the author, Marla Quent, in a dark jacket against a light backdrop"></div>
    <p class="bio">Habitant morbi tristique senectus et. Quis commodo odio aenean sed adipiscing diam. Viverra suspendisse potenti nullam ac tortor. Tincidunt dui ut ornare lectus. Id diam maecenas ultricies mi eget mauris pharetra. Lacus sed viverra tellus in.</p>
    <div class="back-band"></div>
    <p class="back-url">www.marlaquent.com</p>
    <div class="isbn-box" aria-hidden="true"></div>
  </section>

  <section class="panel spine">
    <div class="spine-band"></div>
    <p class="spine-title">The <span class="accent">Plain Harvest</span> Plate</p>
    <span class="spine-mark" aria-hidden="true"></span>
    <p class="spine-author">Marla Quent</p>
  </section>

  <section class="panel front-cover">
    <div class="kitchen-scene" role="img" aria-label="Photo of a fresh Greek salad in a yellow bowl with wooden servers, bottles of olive oil and vinegar on a kitchen counter"></div>
    <h1 class="front-title">
      <span class="small">The</span>
      <span class="big">Plain</span>
      <span class="big">Harvest</span>
      <span class="end">Plate</span>
    </h1>
    <svg class="promise-badge" viewBox="0 0 172 172" aria-hidden="true">
      <defs>
        <radialGradient id="badgeFill" cx="40%" cy="35%" r="70%">
          <stop offset="0%" stop-color="#27b3c2"/>
          <stop offset="100%" stop-color="#0c7683"/>
        </radialGradient>
      </defs>
      <circle cx="86" cy="86" r="80" fill="url(#badgeFill)"/>
      <circle cx="86" cy="86" r="80" fill="none" stroke="#ffffff" stroke-width="3"/>
      <path d="M128 150 Q150 132 160 112 L140 122 Z" fill="#e9ecee"/>
    </svg>
    <p class="badge-text">Reshape Your<br>Bond with Eating<br>in Only <strong>30 DAYS</strong></p>
    <div class="front-band"></div>
    <p class="front-author">Marla Quent</p>
    <div class="author-photo-front" role="img" aria-label="Photo of the author, Marla Quent, smiling, with dark curly hair and a cream jacket"></div>
  </section>

</body>
</html>
```